Business card design for new brand

We have recently rebranded and need a new business card template.

We are an insurance underwriting agency. All of our products are sold via other partner companies, so these are just to pass on our details to other organisations.

We would like to see designs that use the colour green (current stationary generally uses lime green (rgb 142,190,63) and forest green (0,154,79) to comply with our logo's colours. We are happy with other shades of green.

Business cards need to include our logo, as well as space for:
1. Full name
2. Qualifications (optional)
3. Title
4. Office number
5. Mobile number
6. Email address

Our logo is enclosed here.

```html
<!DOCTYPE html>
<html lang="en">
<head>
<meta charset="utf-8">
<title>Verdant Cover – Business Card</title>
<link rel="stylesheet" href="https://fonts.googleapis.com/css2?family=Open+Sans:wght@400;600;700&display=swap">
<style>
  :root {
    --backdrop: #b3a9ab;
    --paper: #ffffff;
    --green: #24dc0e;
    --lime: #7ef20a;
    --ink: #111111;
    --bar: #050308;
    --icon: #17b7c4;
    --pale: #e8ffe0;
  }
  * { margin: 0; padding: 0; box-sizing: border-box; }
  html, body { width: 1200px; height: 960px; overflow: hidden; }
  body {
    background: var(--backdrop);
    font-family: "Open Sans", sans-serif;
    position: relative;
  }
  .card { position: absolute; background: var(--paper); overflow: hidden; }

  /* Front */
  .card-front { left: 253px; top: 46px; width: 678px; height: 388px; }
  .front-brand {
    position: absolute; left: 0; right: 0; top: 180px;
    display: flex; justify-content: center; align-items: center; gap: 16px;
  }
  .brand-mark { width: 40px; height: 40px; background: var(--green); }
  .brand-name {
    font-weight: 600; color: var(--ink); font-size: 54px; letter-spacing: 0.5px; line-height: 1;
  }
  .front-web {
    position: absolute; left: 0; right: 0; top: 322px;
    text-align: center; font-size: 15px; color: var(--ink);
  }
  .front-band-lime { position: absolute; left: 0; right: 0; top: 352px; height: 12px; background: var(--lime); }
  .front-band-green { position: absolute; left: 0; right: 0; top: 364px; height: 24px; background: var(--green); }

  /* Back */
  .card-back { left: 254px; top: 506px; width: 672px; height: 384px; }
  .back-brand {
    position: absolute; left: 58px; top: 200px;
    display: flex; align-items: center; gap: 10px;
  }
  .back-brand .brand-mark { width: 22px; height: 22px; }
  .back-brand .brand-name { font-size: 28px; }
  .back-lime-strip { position: absolute; left: 314px; top: 0; width: 14px; height: 100%; background: var(--lime); }
  .back-panel { position: absolute; left: 328px; top: 0; right: 0; height: 100%; background: var(--green); }
  .name-accent { position: absolute; left: 330px; top: 98px; width: 3px; height: 48px; background: var(--lime); }
  .person-name {
    position: absolute; left: 348px; top: 96px;
    font-weight: 700; font-size: 24px; color: var(--ink); white-space: nowrap;
  }
  .person-qual { font-weight: 400; font-size: 17px; margin-left: 4px; }
  .person-title {
    position: absolute; left: 348px; top: 127px;
    font-size: 15px; color: var(--pale);
  }
  .title-rule { position: absolute; left: 438px; right: 0; top: 136px; height: 1px; background: var(--lime); }

  .contact-row { position: absolute; left: 308px; width: 364px; height: 28px; }
  .contact-row::after {
    content: ""; position: absolute; right: 0; top: 0; width: 14px; height: 100%; background: var(--lime);
  }
  .contact-bar {
    position: absolute; left: 0; top: 0; width: 350px; height: 100%;
    background: var(--bar); display: flex; align-items: center;
  }
  .contact-icon {
    width: 26px; height: 26px; border-radius: 50%; background: var(--paper);
    margin-left: 34px; display: flex; align-items: center; justify-content: center;
  }
  .contact-text { color: var(--paper); font-size: 16px; margin-left: 13px; letter-spacing: 0.3px; }
  .row-office { top: 227px; }
  .row-mobile { top: 272px; }
  .row-email { top: 321px; }
</style>
</head>
<body>
  <section class="card card-front">
    <div class="front-brand">
      <span class="brand-mark"></span>
      <span class="brand-name">Verdant Cover</span>
    </div>
    <p class="front-web">www.verdantcover.com</p>
    <div class="front-band-lime"></div>
    <div class="front-band-green"></div>
  </section>

  <section class="card card-back">
    <div class="back-brand">
      <span class="brand-mark"></span>
      <span class="brand-name">Verdant Cover</span>
    </div>
    <div class="back-lime-strip"></div>
    <div class="back-panel"></div>
    <div class="name-accent"></div>
    <h1 class="person-name">MARCUS HALE<span class="person-qual">MBA</span></h1>
    <p class="person-title">Chief Officer</p>
    <div class="title-rule"></div>

    <div class="contact-row row-office">
      <div class="contact-bar">
        <span class="contact-icon">
          <svg width="16" height="16" viewBox="0 0 24 24" aria-hidden="true">
            <path fill="#17b7c4" d="M6.6 10.8a15.1 15.1 0 0 0 6.6 6.6l2.2-2.2a1 1 0 0 1 1-.25 11.4 11.4 0 0 0 3.6.57 1 1 0 0 1 1 1V20a1 1 0 0 1-1 1A17 17 0 0 1 3 4a1 1 0 0 1 1-1h3.5a1 1 0 0 1 1 1c0 1.25.2 2.45.57 3.57a1 1 0 0 1-.25 1z"/>
          </svg>
        </span>
        <span class="contact-text">732-555-0148</span>
      </div>
    </div>

    <div class="contact-row row-mobile">
      <div class="contact-bar">
        <span class="contact-icon">
          <svg width="14" height="16" viewBox="0 0 14 20" aria-hidden="true">
            <rect x="2" y="1" width="10" height="18" rx="2" fill="none" stroke="#17b7c4" stroke-width="1.8"/>
            <circle cx="7" cy="16" r="1" fill="#17b7c4"/>
          </svg>
        </span>
        <span class="contact-text">732-555-0193</span>
      </div>
    </div>

    <div class="contact-row row-email">
      <div class="contact-bar">
        <span class="contact-icon">
          <svg width="16" height="16" viewBox="0 0 24 24" aria-hidden="true">
            <circle cx="12" cy="12" r="4" fill="none" stroke="#17b7c4" stroke-width="2.4"/>
            <path d="M16 8v5.5a2.5 2.5 0 0 0 5 0V12a9 9 0 1 0-3.5 7.1" fill="none" stroke="#17b7c4" stroke-width="2.4" stroke-linecap="round"/>
          </svg>
        </span>
        <span class="contact-text">hello@verdantcover.com</span>
      </div>
    </div>
  </section>
</body>
</html>
```